Environmental Consulting Project Examples Flyer

We need a flyer designed to promote 3-4 past projects. Each project will have a picture and a paragraph description of it. The final design should convey expertise in out field to potential customers.
Updates

I uploaded a new word document with the project descriptions and a copy of one our business cards for a color/font reference.

Also the project has been guarenteed

Target Market(s)

White collar, male industrial facility managers age 40-60.

Industry/Entity Type

Consulting

Requirements
Must have
• Logo & contact info from www.tarnwick-eco.example

1-2 pages. A place for a photo connecting to each description.

```html
<!DOCTYPE html>
<html lang="en">
<head>
<meta charset="utf-8">
<title>Stormwater General Permit – Project Examples</title>
<link rel="stylesheet" href="https://fonts.googleapis.com/css2?family=Oswald:wght@700&family=Roboto+Condensed:wght@400;700&display=swap">
<style>
  :root {
    --canvas: #ffffff;
    --blue-deep: #1c46d2;
    --blue-light: #4a9cf0;
    --title-red: #c8171c;
    --title-yellow: #ffe21a;
    --text-light: #ffffff;
    --photo-sky: #c9d3dc;
    --photo-yard: #9a958c;
    --photo-site: #b9b4a6;
    --photo-lot: #6f7378;
    --photo-lot-light: #a4a8ad;
    --logo-ink: #2a84d8;
    --logo-mark: #4caf50;
  }
  * { box-sizing: border-box; margin: 0; padding: 0; }
  html, body { width: 1200px; height: 848px; overflow: hidden; background: var(--canvas); }
  body { position: relative; font-family: "Roboto Condensed", "Arial Narrow", sans-serif; }

  .page {
    position: absolute; top: 83px; width: 522px; height: 680px; overflow: hidden;
    box-shadow: 0 6px 14px rgba(0,0,0,.35);
  }
  .page--left { left: 51px; background: var(--blue-deep); }
  .page--right { left: 623px; }

  .photo { position: absolute; }
  .blue-panel {
    position: absolute; color: var(--text-light);
    background: linear-gradient(180deg, var(--blue-deep) 0%, var(--blue-light) 100%);
  }
  .project-title { font-weight: 700; font-size: 13.5px; line-height: 1.25; margin-bottom: 12px; }
  .project-body { font-weight: 700; font-size: 11.6px; line-height: 1.45; text-align: justify; }

  /* left page */
  .photo--lumber { left: 0; top: 0; width: 522px; height: 191px;
    background: linear-gradient(180deg, var(--photo-sky) 0%, #e4e2dc 45%, var(--photo-yard) 100%); }
  .photo--dam-site { left: 192px; top: 191px; width: 330px; height: 286px;
    background: linear-gradient(160deg, #dcd9d0 0%, var(--photo-site) 55%, #8d8a80 100%); }
  .panel--lumber { left: 0; top: 191px; width: 192px; height: 489px; padding: 14px 10px 10px 10px; }
  .panel--dam { left: 192px; top: 477px; width: 330px; height: 203px; padding: 18px 14px 10px 14px; }

  .headline { position: absolute; left: 198px; top: 203px; width: 322px; }
  .headline-line {
    display: block; width: fit-content; margin-left: auto; margin-bottom: 6px;
    background: var(--title-red); color: var(--title-yellow);
    font-family: "Oswald", "Arial Narrow", sans-serif; font-weight: 700;
    font-size: 46px; line-height: 50px; padding: 0 8px; letter-spacing: .5px;
  }

  /* right page */
  .photo--distribution { left: 0; top: 0; width: 522px; height: 680px;
    background: linear-gradient(180deg, #cfd8e0 0%, #e9ecef 10%, var(--photo-lot-light) 22%, var(--photo-lot) 60%, #7c8085 100%); }
  .photo--bottling { left: 371px; top: 395px; width: 151px; height: 222px;
    background: linear-gradient(200deg, #e9e4d6 0%, #b8ac92 50%, #6c6a66 100%); }
  .panel--seattle { left: 97px; top: 151px; width: 425px; height: 226px; padding: 18px 14px 10px 18px; }
  .panel--seattle .project-title { text-align: right; }
  .panel--bottling { left: 0; top: 395px; width: 371px; height: 218px; padding: 18px 14px 10px 14px; overflow: hidden; }

  .brand {
    position: absolute; left: 411px; top: 617px; width: 111px; height: 63px;
    background: var(--canvas); display: flex; align-items: center; justify-content: center; gap: 5px;
  }
  .brand-mark { width: 10px; height: 10px; background: var(--logo-mark); }
  .brand-name { font-weight: 700; font-size: 14px; color: var(--logo-ink); }
</style>
</head>
<body>

<section class="page page--left">
  <div class="photo photo--lumber" role="img" aria-label="Photo of a lumber yard with stacked timber and wrapped pallets"></div>
  <div class="photo photo--dam-site" role="img" aria-label="Photo of excavators working on a snowy dam construction site"></div>

  <h1 class="headline">
    <span class="headline-line">STORMWATER</span>
    <span class="headline-line">GENERAL</span>
    <span class="headline-line">PERMIT</span>
  </h1>

  <article class="blue-panel panel--lumber">
    <h2 class="project-title">Everett Lumber Yard<br>Industrial Stormwater General Permit</h2>
    <p class="project-body">As part of an environmental action group's civil lawsuit, the facility was forced to meet benchmark limits of the industrial stormwater general permit for 8 consecutive quarters. Previous quarters identified pH, turbidity, biological oxygen demand, zinc and copper as the pollutants that exceeded the benchmark limits. To solve the issue, Tarnwick Eco utilized targeted best management practices (BMP's) and identified and addressed the various pollutant sources. With guidance from Tarnwick Eco, the 8 acre facility avoided the costly purchase and installation of an active treatment system while still maintaining full permit compliance.</p>
  </article>

  <article class="blue-panel panel--dam">
    <h2 class="project-title">Halvorsen Ridge Dam<br>Construction Stormwater General Permit</h2>
    <p class="project-body">Maintaining environmental compliance with the Army Corps of Engineers' strict standards during construction on the banks of the City of Tacoma's water supply was a daunting task to be accomplished. Throughout the project Tarnwick Eco kept the site in compliance. After the project was completed Tarnwick Eco performed a final walk-through with the Corps to ensure that no sources of pollution entered the drinking supply when the dewatered construction was put back under water.</p>
  </article>
</section>

<section class="page page--right">
  <div class="photo photo--distribution" role="img" aria-label="Photo of delivery trucks parked at a food distribution center lot"></div>
  <div class="photo photo--bottling" role="img" aria-label="Photo of a beverage bottling plant building with loading docks"></div>

  <article class="blue-panel panel--seattle">
    <h2 class="project-title">Seattle Food Distribution Center<br>Industrial Stormwater General Permit<br>Discharge to 303d Impaired Water Body</h2>
    <p class="project-body">Even though industrial activities are minimal at this distribution facility located on the Duwamish River, meeting the benchmark limits of the industrial stormwater permit has been a struggle. As part of the Level 3 Corrective action, Tarnwick Eco identified ambient sources, approach roads and neighboring facilities as the primary cause of benchmark exceedences of turbidity, copper and zinc. Utilizing cost effective BMP's the facility has maintained compliance while the pollutant sources are addressed.</p>
  </article>

  <article class="blue-panel panel--bottling">
    <h2 class="project-title">Beverage Bottling &amp; Distribution Plant<br>Industrial Stormwater General Permit<br>Discharge to 303d Impaired Water Body</h2>
    <p class="project-body">A high amount of vehicle traffic combined with a large paved facility are a recipe for high zinc and copper sample results. The project goal was to avoid a level 3 corrective action, thus avoiding the installation of an active treatment system. The management at Tarnwick Eco came up with a series of BMP's to maintain</p>
  </article>

  <div class="brand">
    <span class="brand-mark"></span>
    <span class="brand-name">Tarnwick Eco</span>
  </div>
</section>

</body>
</html>
```